new marketing company logo and business card

design logo and biz card for marketing start up.

My company name needs a brand logo designed: Cedar Hollow Marketing Co.
Tagline: Sales - Marketing - Brand Building

Sister Bay is the name of my favorite place, in Wisconsin, but the business is NOT BASED there. It should evoke warmth, friendliness, professionalism, and marketing services from a seasoned marketer.

Target Market(s)

I am selling my services to small business that need help.

Industry/Entity Type

Marketing

Contact Information for Business Card

Cedar Hollow Marketing Co. (logo)
Sales - Marketing - Brand Building (tagline)

Maren T. Holloway
MarenTHolloway@quillpost.net
555-014-3926 mobile

Font styles to use
Serif
Sans Serif

Colors
f78f20
f37122
f68d4d
00a990
85cae6
33b8a4
faa54b

Requirements
Must have
• a logo
• a business card
Nice to have
• I'd love to see a small subtle reference to Sister Bay built in. Sister bay is named that because there are two islands called ‘sister islands’ that flank the bay. If you google this you will see.
• I like warm, earthy colors. But, I am a fun, approachable, real person. Not stand-offish. Should be warm and appealing yet professional.
Should not have
• nothing cartoon-ish. no child-like fonts. this is a professional business.

```html
<!DOCTYPE html>
<html lang="en">
<head>
<meta charset="utf-8">
<title>Cedar Hollow Marketing Co. — Business Card</title>
<link rel="stylesheet" href="https://fonts.googleapis.com/css2?family=Lato:wght@400;700;900&display=swap">
<style>
  :root {
    --backdrop: #3b3b3d;
    --paper: #efefef;
    --orange: #f37122;
    --teal: #33b8a4;
    --ink: #3a3a3a;
    --white: #ffffff;
  }
  * { margin: 0; padding: 0; box-sizing: border-box; }
  html, body {
    width: 1200px; height: 896px; overflow: hidden;
    background: var(--backdrop);
    font-family: "Lato", sans-serif;
  }
  .canvas {
    position: relative; width: 1200px; height: 896px;
    display: flex; flex-direction: column; align-items: center; justify-content: center; gap: 32px;
  }
  .card {
    position: relative; width: 700px; height: 400px; overflow: hidden;
    box-shadow: 0 10px 24px rgba(0,0,0,.35);
  }

  /* Front */
  .card-front {
    background: linear-gradient(200deg, var(--orange) 0%, #b88744 50%, var(--teal) 100%);
    color: var(--white);
    display: flex; flex-direction: column; justify-content: center; padding-left: 96px;
  }
  .front-brand { font-weight: 900; text-transform: uppercase; line-height: 1; }
  .front-brand .brand-line-1 { display: block; font-size: 62px; letter-spacing: 2px; }
  .front-brand .brand-line-2 { display: block; font-size: 31px; letter-spacing: 2px; margin-top: 8px; padding-left: 32px; }
  .front-tagline {
    margin-top: 40px;
    font-size: 18px; font-weight: 400; letter-spacing: 1px; text-transform: uppercase;
  }

  /* Back */
  .card-back { background: var(--paper); }
  .back-swoosh { position: absolute; inset: 0; width: 700px; height: 400px; }
  .holder-name {
    position: absolute; left: 160px; top: 44px;
    font-size: 26px; font-weight: 700; text-transform: uppercase; letter-spacing: 1px;
    color: var(--orange);
  }
  .holder-name .first { color: var(--teal); }
  .contact-list {
    position: absolute; left: 100px; top: 112px; list-style: none;
    font-size: 19px; color: var(--ink); line-height: 1.35;
  }
  .contact-list li { display: flex; align-items: center; gap: 8px; }
  .contact-list svg { width: 18px; height: 18px; flex: none; }
  .back-brand {
    position: absolute; right: 40px; top: 150px; width: 200px;
    display: flex; align-items: center; gap: 12px;
    font-size: 22px; font-weight: 900; color: var(--orange); line-height: 1.15;
  }
  .back-brand .brand-dot {
    width: 30px; height: 30px; border-radius: 50%; background: var(--teal); flex: none;
  }
  .back-tagline {
    position: absolute; left: 250px; top: 318px;
    font-size: 17px; font-weight: 400; letter-spacing: 1px; text-transform: uppercase;
    color: var(--white); transform: rotate(7deg); transform-origin: left center; white-space: nowrap;
  }
</style>
</head>
<body>
<main class="canvas">
  <section class="card card-front" aria-label="Card front">
    <h1 class="front-brand">
      <span class="brand-line-1">Cedar Hollow</span>
      <span class="brand-line-2">Marketing Co.</span>
    </h1>
    <p class="front-tagline">Sales - Marketing - Brand Building</p>
  </section>

  <section class="card card-back" aria-label="Card back">
    <svg class="back-swoosh" viewBox="0 0 700 400" aria-hidden="true">
      <path d="M0,128 C120,205 330,268 610,322 L610,400 L0,400 Z" fill="var(--teal)"/>
      <path d="M0,174 C200,244 450,264 700,338 L700,400 L0,400 Z" fill="var(--white)"/>
      <path d="M0,180 C200,250 450,270 700,344 L700,400 L0,400 Z" fill="var(--orange)"/>
    </svg>

    <h2 class="holder-name"><span class="first">Maren</span> T. Holloway</h2>
    <ul class="contact-list">
      <li>
        <svg viewBox="0 0 24 24" aria-hidden="true"><path fill="var(--teal)" d="M6.6 10.8a15 15 0 0 0 6.6 6.6l2.2-2.2a1 1 0 0 1 1-.25 11.4 11.4 0 0 0 3.6.57 1 1 0 0 1 1 1V20a1 1 0 0 1-1 1A17 17 0 0 1 3 4a1 1 0 0 1 1-1h3.5a1 1 0 0 1 1 1c0 1.25.2 2.45.57 3.57a1 1 0 0 1-.25 1z"/></svg>
        555-014-3926
      </li>
      <li>
        <svg viewBox="0 0 24 24" aria-hidden="true"><rect x="2" y="5" width="20" height="14" rx="1" fill="var(--teal)"/><path d="M2 6l10 7 10-7" fill="none" stroke="var(--paper)" stroke-width="1.6"/></svg>
        MarenTHolloway@quillpost.net
      </li>
    </ul>

    <div class="back-brand">
      <span class="brand-dot" aria-hidden="true"></span>
      <span>Cedar Hollow Marketing Co.</span>
    </div>

    <p class="back-tagline">Sales - Marketing - Brand Building</p>
  </section>
</main>
</body>
</html>
```